Ridgeway Insulcoat Works Spray Foam Appications website

We need a custom website for our company, www.ridgewayinsulcoatworks.example. We need something we can modify by adding/changing content, photos, updated projects, etc. We are a commercial contractor specializing in Spray Foam applications. We want the website to be very creative and easy to navigate. The main points of the website are to showcase our projects, and describe our scope of services. We provide spray foam applications to the residential and commercial market. We offer Spray Foam roofing applications, as well as Spray Foam interior insulation applications. We also provide Roof Restoration Coating Systems to refurbish old and failing metal roofs. We would be ok with a one page web design if we can get the scope of our services to flow in a single page. The designer can decide if single or multiple pages works best for our business. One of the suppliers we work with is www.vantrexo.example.

Target Market(s)

Residential Home Builders, General Contractors, Commercial Construction Companies, Property Management Groups.

Industry/Entity Type

Insulation

Number of Pages Required

5+ page

Font styles to use
Serif
Sans Serif

Colors

Designer to choose colors to be used in the design.

Requirements
Must have
• We already have a Wix page, so website must be a Wix theme design. Nice easy to navigate format. Color matched to our current logo theme. We already have brochures and would like for it to match what's already in the hands of some of our customers. Need to be able to manage content to update photos, projects, scope of service, etc., via Wix. Current hold/splash page is hosted at www.ridgewayinsulcoatworks.example. We would also like to have this video posted on the home page: https://www.videohost.example/watch?v=QzT4kLp9wXe&feature=share
Nice to have
• I have attached some splash videos, being able to incorporate these somehow without being overpowering would be nice.

```html
<!DOCTYPE html>
<html lang="en">
<head>
<meta charset="utf-8">
<title>Ridgeway Insulcoat Works</title>
<link href="https://fonts.googleapis.com/css2?family=Mulish:wght@400;600;700;800;900&display=swap" rel="stylesheet">
<style>
:root{
  --orange:#eea319;
  --ink:#111111;
  --text:#2b2b2b;
  --card:#f4f4f4;
  --panel:#f3f3f3;
  --field:#ffffff;
  --white:#ffffff;
}
*{margin:0;padding:0;box-sizing:border-box}
html,body{width:1200px;height:4283px;overflow:hidden;background:var(--white)}
body{font-family:'Mulish',Arial,sans-serif;color:var(--text)}
.page{position:relative;width:1200px;height:4283px;overflow:hidden}
.abs{position:absolute}

/* header */
.site-header{position:absolute;left:0;top:0;width:1200px;height:96px;background:var(--white)}
.brand{position:absolute;left:156px;top:18px;display:flex;align-items:center;gap:10px}
.brand-ring{width:60px;height:60px;border:4px solid var(--orange);border-radius:50%;flex:none}
.brand-name{font-weight:800;font-size:17px;color:var(--orange);letter-spacing:.2px;white-space:nowrap}
.nav a{position:absolute;top:38px;font-size:15px;color:var(--ink);text-decoration:none;letter-spacing:.3px}
.nav a.active{font-weight:800}

/* hero */
.hero{position:absolute;left:0;top:96px;width:1200px;height:669px;
  background:
    radial-gradient(ellipse 300px 360px at 150px 260px,rgba(184,122,38,.9),rgba(150,98,34,.55) 55%,rgba(0,0,0,0) 100%),
    radial-gradient(ellipse 520px 200px at 700px 250px,rgba(122,112,100,.7),rgba(0,0,0,0) 100%),
    linear-gradient(180deg,#3b2f5a 0%,#564a6a 18%,#6a5d55 38%,#7a7468 58%,#5d5b4e 78%,#4f7a2e 90%,#3f6a24 100%)}
.hero-title{position:absolute;left:0;top:262px;width:1200px;text-align:center;color:var(--white);
  font-weight:900;font-size:46px;line-height:50px;letter-spacing:.5px}

/* section titles */
.section-title{position:absolute;left:0;width:1200px;text-align:center;font-weight:900;font-size:32px;color:var(--ink)}
.rule{position:absolute;height:5px;width:66px;background:var(--orange)}

/* services */
.service-card{position:absolute;top:896px;width:293px;height:414px;background:var(--card)}
.service-photo{height:201px;width:100%}
.service-body{padding:22px 0 0 36px}
.service-body h3{font-size:20px;line-height:25px;font-weight:700;color:var(--ink);margin-bottom:10px}
.service-body li{list-style:none;font-size:13.5px;line-height:20.5px;color:#333}

/* about */
.about-panel{position:absolute;left:0;top:1413px;width:590px;height:555px;background:var(--orange)}
.about-panel h2{position:absolute;left:128px;top:84px;font-size:32px;font-weight:900;color:var(--white)}
.about-panel .rule{left:124px;top:129px;background:var(--white);width:60px;height:3px}
.about-panel p{position:absolute;left:121px;width:410px;font-size:15px;line-height:23px;color:var(--white)}
.about-photo{position:absolute;left:590px;top:1413px;width:610px;height:555px;
  background:
    radial-gradient(ellipse 380px 120px at 380px 150px,rgba(190,160,120,.85),rgba(0,0,0,0) 100%),
    linear-gradient(180deg,#1f3c8e 0%,#3457a6 20%,#8d8a82 32%,#bdb9ae 42%,#d9d3b0 55%,#dccb85 72%,#c3ad62 100%)}

/* projects */
.project-photo{position:absolute;width:442px;height:400px}

/* contact */
.contact{position:absolute;left:0;top:3075px;width:1200px;height:1130px;background:var(--panel)}
.map{position:absolute;left:191px;top:3208px;width:821px;height:324px;
  background:
    radial-gradient(ellipse 200px 80px at 640px 250px,rgba(200,200,200,.8),rgba(0,0,0,0) 100%),
    linear-gradient(135deg,#e4e4e4 0%,#f0f0f0 40%,#e8e8e8 70%,#dedede 100%)}
.col-title{position:absolute;font-size:25px;font-weight:700;color:var(--ink)}
.small{position:absolute;font-size:13.5px;line-height:27px;color:#222}
.label{position:absolute;left:204px;font-size:13.5px;color:#222}
.field{position:absolute;left:201px;width:354px;background:var(--field);font-size:12px;color:#777;padding:10px 14px}
.submit{position:absolute;left:420px;top:4104px;width:135px;height:36px;background:var(--orange);
  color:var(--ink);font-size:12px;font-weight:800;text-align:center;line-height:36px}
.quote{position:absolute;left:653px;font-weight:700;color:var(--ink)}

/* footer */
.copyright{position:absolute;left:201px;top:4238px;font-size:13.5px;color:#333}
.social{position:absolute;top:4225px;width:34px;height:34px;border:2px solid var(--ink);border-radius:50%}
</style>
</head>
<body>
<div class="page">

  <header class="site-header">
    <div class="brand">
      <span class="brand-ring"></span>
      <span class="brand-name">Ridgeway Insulcoat Works</span>
    </div>
    <nav class="nav">
      <a class="active" href="#" style="left:500px">HOME</a>
      <a href="#" style="left:592px">SERVICES</a>
      <a href="#" style="left:710px">ABOUT</a>
      <a href="#" style="left:808px">PROJECTS</a>
      <a href="#" style="left:927px">CONTACT US</a>
    </nav>
  </header>

  <section class="hero" role="img" aria-label="Evening view of a stucco and stone home with an autumn tree in front">
    <svg class="abs" style="left:556px;top:153px" width="84" height="84" viewBox="0 0 84 84" aria-hidden="true">
      <circle cx="42" cy="42" r="36" fill="none" stroke="#eea319" stroke-width="5"/>
      <circle cx="42" cy="42" r="27" fill="#ffffff"/>
      <path d="M35 29 L55 42 L35 55 Z" fill="#111111"/>
    </svg>
    <h1 class="hero-title">WELCOME TO<br>RIDGEWAY INSULCOAT WORKS</h1>
    <svg class="abs" style="left:578px;top:408px" width="44" height="26" viewBox="0 0 44 26" aria-hidden="true">
      <path d="M3 3 L22 22 L41 3" fill="none" stroke="#ffffff" stroke-width="4"/>
    </svg>
  </section>

  <h2 class="section-title" style="top:815px">OUR SERVICES</h2>
  <div class="rule" style="left:567px;top:863px"></div>

  <article class="service-card" style="left:136px">
    <div class="service-photo" role="img" aria-label="Worker spraying white foam on a metal roof" style="background:linear-gradient(180deg,#55606e 0%,#6f746f 22%,#9a9a8e 34%,#e2e3e4 52%,#c7c9cb 78%,#a9acaf 100%)"></div>
    <div class="service-body">
      <h3>Spray Foam Roofing<br>Applications</h3>
      <ul><li>Life time Maintainable system</li><li>Seamless self-adhering system</li><li>Weather durability</li><li>Repair vs Replace</li></ul>
    </div>
  </article>
  <article class="service-card" style="left:454px">
    <div class="service-photo" role="img" aria-label="Interior wall freshly sprayed with foam insulation" style="background:linear-gradient(180deg,#7a6f5e 0%,#bdb6a6 18%,#dcd8cb 40%,#cfcbbf 62%,#8f8d88 78%,#5e5c58 100%)"></div>
    <div class="service-body">
      <h3>Spray Foam<br>Interior Insulation</h3>
      <ul><li>Improve energy efficiency up to 45%</li><li>energy savings</li><li>Maintain consistent temperatures</li><li>Increase racking strength</li></ul>
    </div>
  </article>
  <article class="service-card" style="left:773px">
    <div class="service-photo" role="img" aria-label="Coated metal roof under a blue sky" style="background:linear-gradient(180deg,#2c4f9e 0%,#4a6cb0 30%,#8090ad 42%,#b8bcc3 55%,#8d939c 80%,#6c727b 100%)"></div>
    <div class="service-body">
      <h3>Roof Restoration<br>Coating Systems</h3>
      <ul><li>Repair without replacing Eliminates</li><li>tear offs</li><li>Warranties availbale</li><li>Energy Savings</li></ul>
    </div>
  </article>

  <section class="about-panel">
    <h2>ABOUT US</h2>
    <div class="rule"></div>
    <p style="top:154px">Nunc tempus felis vitae urna Vivamus porttitor neque at volutpat rutrum purus nisi eleifend libero a tempus libero lectus feugiat felis Morbi diam mauris viverra in gravida eu mattis in ante Morbi eget arcu Morbi porta libero id ullamcorper nonummy nibh ligula pulvinar</p>
    <p style="top:292px">Aetus eget consectetuer augue nisi quis lacus Ut ac mi quis lacus mollis aliquam Curabitur iaculis tempus eros Curabitur vel mi sit amet magna malesuada ultricies Ut nisi erat fermentum vel congue id euismod in elit Fusce ultricies orci ac feugiat suscipit leo massa sodales velit et scelerisque mi tortor at ipsum Proin orci odio</p>
  </section>
  <div class="about-photo" role="img" aria-label="Industrial building with a yellow spray foam roof in progress"></div>

  <h2 class="section-title" style="top:2027px">OUR PROJECTS</h2>
  <div class="rule" style="left:567px;top:2074px"></div>

  <div class="project-photo" role="img" aria-label="Worker on a white foam coated roof" style="left:143px;top:2126px;background:linear-gradient(180deg,#5d6470 0%,#747570 18%,#a09c8c 28%,#e3e4e6 45%,#cfd1d3 70%,#b2b4b7 100%)"></div>
  <div class="project-photo" role="img" aria-label="Ribbed metal roof with grey coating beside a plant" style="left:617px;top:2126px;background:linear-gradient(180deg,#4169ac 0%,#7893bd 12%,#7d8462 22%,#a8a9a6 34%,#939597 62%,#6e7073 100%)"></div>
  <div class="project-photo" role="img" aria-label="Freshly coated white roof next to an industrial structure" style="left:143px;top:2555px;background:linear-gradient(180deg,#2c3139 0%,#6f7883 18%,#a7adb4 30%,#dfe1e3 46%,#c4c6c9 64%,#85878b 100%)"></div>
  <div class="project-photo" role="img" aria-label="Yellow foam roof with an orange marker cone" style="left:617px;top:2555px;background:linear-gradient(180deg,#1f4da0 0%,#4570b4 26%,#7a7e76 36%,#d2c891 50%,#d7c681 70%,#b09c58 100%)"></div>

  <section class="contact">
    <h2 class="section-title" style="top:56px">CONTACT US</h2>
    <div class="rule" style="left:571px;top:103px"></div>
  </section>

  <div class="map" role="img" aria-label="Street map with a location pin marking the office"></div>
  <svg class="abs" style="left:572px;top:3345px" width="36" height="48" viewBox="0 0 36 48" aria-hidden="true">
    <path d="M18 2 C8 2 2 9 2 18 C2 30 18 46 18 46 C18 46 34 30 34 18 C34 9 28 2 18 2 Z" fill="#111111"/>
    <circle cx="18" cy="18" r="6" fill="#ffffff"/>
  </svg>

  <h3 class="col-title" style="left:201px;top:3578px">Inquiries</h3>
  <p class="small" style="left:201px;top:3614px">For any inquiries, questions or commendations, please call:<br>555-014-2290 or fill out the following form</p>

  <h3 class="col-title" style="left:658px;top:3578px">Our Address</h3>
  <p class="small" style="left:658px;top:3614px">218 Larkmoor Avenue<br>Fairbridge, CA 95021</p>

  <p class="small" style="left:658px;top:3699px;line-height:28.5px">hello@ridgewayinsulcoat.example<br>Tel: 555-014-2290<br>Fax: 555-014-2291</p>

  <p class="quote" style="top:3830px;font-size:22px">Get a Quote Now</p>
  <p class="quote" style="top:3868px;font-size:21px">555-014-2290</p>

  <h3 class="col-title" style="left:201px;top:3706px">Contact Us</h3>
  <form>
    <label class="label" style="top:3752px">Enter Your Name</label>
    <div class="field" style="top:3779px;height:39px">Name</div>
    <label class="label" style="top:3838px">Enter Your Email</label>
    <div class="field" style="top:3864px;height:39px">Email</div>
    <label class="label" style="top:3923px">Enter Your Subject</label>
    <div class="field" style="top:3951px;height:38px">Subject</div>
    <div class="field" style="top:4006px;height:86px">Message</div>
    <div class="submit">SUBMIT</div>
  </form>

  <footer>
    <p class="copyright">© 2020 Company Name | All Rights Reserved</p>
    <span class="social" style="left:942px" aria-label="Social link"></span>
    <span class="social" style="left:981px" aria-label="Social link"></span>
    <span class="social" style="left:1020px" aria-label="Social link"></span>
  </footer>

</div>
</body>
</html>
```